8"x5" postcard for Wireless Internet introduction to new mountain town market

I need to market high speed internet to a resort mountain town without doing the obvious laptop on a mountain top thing, so tired. We are going to be competing directly with another provider with same cost, but we will be offering free installation. The area is Aspen Colorado, so the clientele are outdoor types who have suffered for years from being disconnected in their mountain town. We offer fast internet and excellent customer service from people who live in their neck of the woods.

Target Market(s)

23-55 years old, both resort living, families and ski bums

Font styles to use
Sans Serif

Colors

Designer to choose colors to be used in the design.

Requirements
Must have
• Visual appeal and fresh verbiage. We don't mind being a little edgy. We are a young company and we want to appeal to people looking for a provider who gets them. We prefer a clean look.
Nice to have
• Nice to have colors that match our logo
Should not have
• stuffy concepts or verbiage that is too much like a car salesman. We don't want to look like a 'big box' company.

```html
<!DOCTYPE html>
<html lang="en">
<head>
<meta charset="UTF-8">
<title>Ridgeline Broadband Postcard</title>
<link rel="stylesheet" href="https://fonts.googleapis.com/css2?family=Montserrat:wght@300;400;800;900&family=Poppins:wght@500;600&display=swap">
<style>
  :root {
    --bg: #6b6b6b;
    --bg-light: #8e8e8e;
    --white: #ffffff;
    --ink: #1c1b1d;
    --yellow: #f6d21f;
    --yellow-deep: #e8c214;
    --orange: #fbb040;
    --slate: #5b5f6b;
    --blue-deep: #0d3f73;
    --blue-light: #59b9e6;
  }
  * { margin: 0; padding: 0; box-sizing: border-box; }
  html, body { width: 1200px; height: 1200px; overflow: hidden; }
  body {
    background: radial-gradient(circle at 50% 40%, var(--bg-light), var(--bg) 70%);
    font-family: "Poppins", sans-serif;
  }
  .postcard {
    position: absolute;
    left: 50px; top: 256px;
    width: 1100px; height: 688px;
    background: var(--white);
    overflow: hidden;
    box-shadow: 0 18px 40px rgba(0,0,0,0.35);
  }
  .postcard-shapes { position: absolute; inset: 0; }
  .brand {
    position: absolute; left: 40px; top: 30px;
    display: flex; align-items: center; gap: 16px;
  }
  .brand-dot {
    width: 76px; height: 76px; border-radius: 50%;
    background: var(--orange); flex: none;
  }
  .brand-name {
    font-family: "Montserrat", sans-serif;
    font-weight: 800; font-size: 32px; letter-spacing: 1px;
    color: var(--slate); line-height: 1.05;
  }
  .brand-name span { display: block; }
  .headline {
    position: absolute; left: 50px; top: 150px;
    font-family: "Montserrat", sans-serif; font-weight: 900;
    line-height: 1;
  }
  .headline-top { display: block; font-size: 58px; color: var(--ink); letter-spacing: 1px; }
  .headline-big { display: block; font-size: 118px; color: var(--yellow); margin-top: 6px; letter-spacing: -1px; }
  .features {
    position: absolute; left: 40px; top: 375px;
    list-style: none;
  }
  .features li {
    display: flex; align-items: center; gap: 14px;
    font-weight: 500; font-size: 26px; color: var(--ink);
    height: 48px;
  }
  .tick { width: 24px; height: 24px; flex: none; }
  .call {
    position: absolute; left: 36px; top: 594px;
    display: flex; align-items: center; gap: 22px; height: 56px;
  }
  .call-label {
    font-family: "Montserrat", sans-serif; font-weight: 300;
    font-size: 40px; color: var(--yellow); letter-spacing: 1px;
  }
  .call-number {
    display: flex; align-items: center; gap: 10px;
    font-family: "Montserrat", sans-serif; font-weight: 800;
    font-size: 40px; color: var(--white);
  }
  .phone-icon { width: 32px; height: 32px; }
  .web {
    position: absolute; left: 770px; top: 600px;
    display: flex; align-items: center; gap: 14px;
    font-family: "Montserrat", sans-serif; font-weight: 800;
    font-size: 22px; letter-spacing: 3px; color: var(--white);
    height: 44px; white-space: nowrap;
  }
  .web-arrow { width: 22px; height: 22px; flex: none; }
</style>
</head>
<body>
  <main class="postcard">
    <svg class="postcard-shapes" width="1100" height="688" viewBox="0 0 1100 688">
      <defs>
        <linearGradient id="familyTone" x1="0" y1="0" x2="1" y2="1">
          <stop offset="0" stop-color="#dfe3e6"/>
          <stop offset="0.5" stop-color="#8a93a3"/>
          <stop offset="1" stop-color="#3f4656"/>
        </linearGradient>
        <linearGradient id="techTone" x1="0" y1="0" x2="1" y2="1">
          <stop offset="0" stop-color="#59b9e6"/>
          <stop offset="0.55" stop-color="#1f76b4"/>
          <stop offset="1" stop-color="#0d3f73"/>
        </linearGradient>
        <linearGradient id="bandTone" x1="0" y1="0" x2="1" y2="0">
          <stop offset="0" stop-color="#e8c214"/>
          <stop offset="1" stop-color="#f6d21f"/>
        </linearGradient>
      </defs>
      <polygon class="features-band" points="0,357 640,357 500,594 0,594" fill="url(#bandTone)"/>
      <g role="img" aria-label="Photo of a smiling family sharing a laptop on a sofa">
        <polygon points="560,0 1100,0 1100,392 420,150" fill="url(#familyTone)"/>
      </g>
      <polygon points="520,0 560,0 440,150 420,150" fill="#f6d21f"/>
      <polygon points="420,150 1100,392 1100,430 500,172" fill="#fbb040"/>
      <g role="img" aria-label="Photo of a hand on a glowing mouse with network icons">
        <polygon points="672,262 1100,445 1100,594 500,594" fill="url(#techTone)"/>
      </g>
      <polygon points="700,580 1100,580 1100,688 660,688" fill="#fbb040"/>
      <polygon points="0,594 720,594 680,652 0,652" fill="#1c1b1d"/>
      <rect x="0" y="652" width="1100" height="36" fill="#fbb040"/>
    </svg>

    <div class="brand">
      <span class="brand-dot"></span>
      <span class="brand-name"><span>RIDGELINE</span><span>BROADBAND</span></span>
    </div>

    <h1 class="headline">
      <span class="headline-top">BETTER, NOT</span>
      <span class="headline-big">BIGGER!</span>
    </h1>

    <ul class="features">
      <li><svg class="tick" viewBox="0 0 24 24"><circle cx="12" cy="12" r="12" fill="#1c1b1d"/><path d="M6.5 12.5l3.5 3.5 7-7.5" fill="none" stroke="#f6d21f" stroke-width="3" stroke-linecap="round" stroke-linejoin="round"/></svg>Free residential Installation</li>
      <li><svg class="tick" viewBox="0 0 24 24"><circle cx="12" cy="12" r="12" fill="#1c1b1d"/><path d="M6.5 12.5l3.5 3.5 7-7.5" fill="none" stroke="#f6d21f" stroke-width="3" stroke-linecap="round" stroke-linejoin="round"/></svg>In-House Tech Support</li>
      <li><svg class="tick" viewBox="0 0 24 24"><circle cx="12" cy="12" r="12" fill="#1c1b1d"/><path d="M6.5 12.5l3.5 3.5 7-7.5" fill="none" stroke="#f6d21f" stroke-width="3" stroke-linecap="round" stroke-linejoin="round"/></svg>10, 25 and 40Mbps speeds</li>
      <li><svg class="tick" viewBox="0 0 24 24"><circle cx="12" cy="12" r="12" fill="#1c1b1d"/><path d="M6.5 12.5l3.5 3.5 7-7.5" fill="none" stroke="#f6d21f" stroke-width="3" stroke-linecap="round" stroke-linejoin="round"/></svg>Prices start at $59.95</li>
    </ul>

    <div class="call">
      <span class="call-label">CALL NOW!</span>
      <span class="call-number">
        <svg class="phone-icon" viewBox="0 0 24 24"><path d="M6.6 10.8c1.4 2.8 3.8 5.1 6.6 6.6l2.2-2.2c.3-.3.7-.4 1-.2 1.1.4 2.300.6 3.6.6.6 0 1 .4 1 1V20c0 .6-.4 1-1 1C10.6 21 3 13.4 3 4c0-.6.4-1 1-1h3.5c.6 0 1 .4 1 1 0 1.3.2 2.5.6 3.6.1.3 0 .7-.2 1L6.6 10.8z" fill="#f6d21f"/></svg>
        1 888 555 0142
      </span>
    </div>

    <div class="web">
      <svg class="web-arrow" viewBox="0 0 22 22"><circle cx="11" cy="11" r="11" fill="#1c1b1d"/><path d="M9 6.5l4.5 4.5L9 15.5" fill="none" stroke="#ffffff" stroke-width="2.6" stroke-linecap="round" stroke-linejoin="round"/></svg>
      www.rdgn.net/go
    </div>
  </main>
</body>
</html>
```